New design for Gift Ledger Website - landing page plus 3 carousel pages

We have a new website we want to launch for 501c3 organizations - Faith-based organizations, not for profit organizations, colleges and universities. Note - this is a design only project. We want to see designs for the landing page and the 3 other pages - Faith-based organizations, not for profit organizations, colleges and universities.
Format: We expect to create this website in Wix so requirement is to make the graphics Wix compatible
See Dossier attached for more details, 4 wireframes (1 landing page and 3 carousel pages), and brand guidelines
Please be creative and and make the visuals engaging. We do NOT want you to simply replicate what is in the wireframe. We are looking for a totally new, fresh and engaging design.
Look and feel
Each slider illustrates characteristics of the customer's brand and the style your logo design should communicate.

```html
<!DOCTYPE html>
<html lang="en">
<head>
<meta charset="UTF-8">
<title>Non Profits Organization</title>
<link rel="stylesheet" href="https://fonts.googleapis.com/css2?family=Quicksand:wght@400;500;700&display=swap">
<style>
  :root {
    --page-bg: #0c101e;
    --glow-blue: #0a2a8c;
    --teal: #00c9a2;
    --teal-mid: #0a9aa8;
    --royal-blue: #1640c4;
    --deep-blue: #0332a8;
    --text-light: #f2f4f8;
  }
  * { margin: 0; padding: 0; box-sizing: border-box; }
  html, body { width: 1200px; height: 853px; overflow: hidden; background: var(--page-bg); }
  .landing {
    position: relative;
    width: 1200px;
    height: 853px;
    overflow: hidden;
    background:
      radial-gradient(ellipse 420px 620px at 1120px 380px, rgba(10, 42, 170, 0.75), rgba(12, 16, 30, 0) 75%),
      var(--page-bg);
    font-family: "Quicksand", sans-serif;
  }
  .hero-illustration {
    position: absolute;
    left: 600px;
    top: 0;
    width: 540px;
    height: 770px;
    background:
      radial-gradient(ellipse 200px 260px at 210px 590px, rgba(0, 201, 162, 0.75), rgba(0, 201, 162, 0) 75%),
      radial-gradient(ellipse 160px 220px at 120px 80px, rgba(0, 180, 150, 0.6), rgba(0, 180, 150, 0) 75%),
      radial-gradient(ellipse 230px 360px at 290px 330px, rgba(22, 64, 220, 0.9), rgba(22, 64, 220, 0) 80%);
    filter: blur(2px);
  }
  .hero-title {
    position: absolute;
    left: 90px;
    top: 204px;
    font-weight: 400;
    font-size: 69px;
    line-height: 64px;
    letter-spacing: 0.5px;
  }
  .hero-title span {
    display: block;
    width: max-content;
    color: var(--teal);
    -webkit-background-clip: text;
    background-clip: text;
    -webkit-text-fill-color: transparent;
  }
  .hero-title .line-one {
    background-image: linear-gradient(90deg, var(--teal) 0%, var(--teal) 50%, var(--teal-mid) 75%, var(--royal-blue) 100%);
  }
  .hero-title .line-two {
    background-image: linear-gradient(90deg, var(--teal) 0%, var(--teal) 35%, var(--teal-mid) 70%, var(--deep-blue) 100%);
  }
  .hero-intro {
    position: absolute;
    left: 91px;
    top: 366px;
    width: 600px;
    color: var(--text-light);
    font-size: 15.2px;
    line-height: 20px;
    font-weight: 400;
  }
  .feature-icons {
    position: absolute;
    left: 91px;
    top: 528px;
    display: flex;
    gap: 41px;
    list-style: none;
  }
  .feature-icon {
    width: 127px;
    height: 114px;
    border: 1px solid var(--teal);
    border-radius: 4px;
    display: flex;
    align-items: center;
    justify-content: center;
    color: var(--teal);
    font-weight: 700;
    font-size: 31px;
    padding-top: 2px;
  }
</style>
</head>
<body>
  <main class="landing">
    <div class="hero-illustration" role="img" aria-label="Low-poly wireframe illustration of two hands clasped together in teal and blue"></div>
    <h1 class="hero-title">
      <span class="line-one">NON PROFITS</span>
      <span class="line-two">ORGANIZATION</span>
    </h1>
    <p class="hero-intro">Lorem Ipsum is simply dummy text of the printing and typesetting industry. Lorem Ipsum has been the industry's standard dummy text ever since the 1500s, when an unknown printer took a galley of type and scrambled it to make a type specimen book. It has survived not only five centuries, but also the leap into electronic typesetting,</p>
    <ul class="feature-icons">
      <li class="feature-icon">icon</li>
      <li class="feature-icon">icon</li>
      <li class="feature-icon">icon</li>
    </ul>
  </main>
</body>
</html>
```